KV Media Group stationary project
don't have one
Use same font as used in my logo
logo attached
Molly Brennan
President/CEO
don't have one yet
mbrennan@kvmediagroupexample.com
www.kvmediagroupexample.com
I don't have an address yet so can you do an A & B version so I know what it will look like and can add the address at a later date. Also, as part of this contest which includes business card/letterhead/envelopes, can you also do a design for invoice and fax sheet. Thanks!

```html
<!DOCTYPE html>
<html lang="en">
<head>
<meta charset="utf-8">
<title>KV Media Group — Business Card</title>
<link rel="stylesheet" href="https://fonts.googleapis.com/css2?family=Open+Sans:wght@400;600&display=swap">
<style>
  :root {
    --bg: #e9e6e1;
    --card: #ffffff;
    --ink: #3a3a3a;
    --muted: #6b6b6b;
    --orange: #f5a623;
    --orange-pale: #fdebc8;
  }
  * { box-sizing: border-box; margin: 0; padding: 0; }
  html, body { width: 1200px; height: 646px; overflow: hidden; }
  body {
    background: var(--bg);
    font-family: "Open Sans", sans-serif;
    color: var(--ink);
    display: flex;
    align-items: center;
    justify-content: center;
    gap: 60px;
  }
  .card {
    position: relative;
    width: 520px;
    height: 297px;
    background: var(--card);
    box-shadow: 0 6px 18px rgba(0,0,0,0.15);
    overflow: hidden;
  }

  .brand-name {
    font-family: "Open Sans", sans-serif;
    font-weight: 600;
    color: var(--ink);
    white-space: nowrap;
  }

  /* Back side */
  .card--back .brand-name {
    position: absolute;
    left: 50%; top: 44%;
    transform: translate(-50%, -50%);
    font-size: 26px;
  }
  .back-web {
    position: absolute; left: 26px; bottom: 20px;
    font-size: 11px; color: var(--muted);
  }

  /* Front side */
  .card--front .brand-name {
    position: absolute; left: 32px; top: 36px;
    font-size: 20px;
  }

  .title-bar {
    position: absolute; right: 0; top: 92px;
    width: 210px; height: 44px;
    background: var(--orange-pale);
    border-right: 8px solid var(--orange);
    padding: 6px 12px;
    text-align: right;
  }
  .person-name {
    font-weight: 600; font-size: 13px; line-height: 17px; color: var(--orange);
  }
  .person-title { font-size: 10px; line-height: 14px; font-weight: 600; color: var(--ink); }

  .address {
    position: absolute; left: 32px; top: 118px;
    font-size: 11px; line-height: 1.5; color: var(--muted);
  }
  .contacts {
    position: absolute; left: 32px; bottom: 26px;
    list-style: none; font-size: 11px; color: var(--muted);
  }
  .contacts li { display: flex; align-items: center; gap: 8px; line-height: 20px; }
  .contacts .icon {
    width: 12px; height: 12px; border-radius: 50%;
    background: var(--orange); display: inline-flex;
    align-items: center; justify-content: center;
  }
</style>
</head>
<body>

  <section class="card card--back" aria-label="Card back">
    <p class="brand-name">KV Media Group</p>
    <p class="back-web">www.kvmediagroupexample.com</p>
  </section>

  <section class="card card--front" aria-label="Card front">
    <p class="brand-name">KV Media Group</p>

    <div class="title-bar">
      <p class="person-name">Molly Brennan</p>
      <p class="person-title">President/CEO</p>
    </div>

    <p class="address">Suite 1024 Street name,<br>State, Zip 20254 Country</p>

    <ul class="contacts">
      <li>
        <span class="icon"><svg width="8" height="8" viewBox="0 0 10 10"><path d="M2 1l2 2-1 1.5c.6 1.2 1.3 1.9 2.5 2.5L7 6l2 2-1.5 1.5C4 9 1 6 .5 2.5z" fill="#fff"/></svg></span>
        555-010-2468
      </li>
      <li>
        <span class="icon"><svg width="8" height="8" viewBox="0 0 10 10"><rect x="1" y="2.5" width="8" height="5.5" fill="none" stroke="#fff" stroke-width="1.2"/><path d="M1 2.5l4 3 4-3" fill="none" stroke="#fff" stroke-width="1.2"/></svg></span>
        mbrennan@kvmediagroupexample.com
      </li>
      <li>
        <span class="icon"><svg width="8" height="8" viewBox="0 0 10 10"><circle cx="5" cy="5" r="3.8" fill="none" stroke="#fff" stroke-width="1.2"/><path d="M1.2 5h7.6M5 1.2v7.6" stroke="#fff" stroke-width="1"/></svg></span>
        www.kvmediagroupexample.com
      </li>
    </ul>
  </section>

</body>
</html>
```